International wholesale business needs a business card

We need a business card.

Company Details:
Company Name and logo
Address, Phone number, Website
Employee Details:
Name, Designation, Mobile Number & Email address

```html
<!DOCTYPE html>
<html lang="en">
<head>
<meta charset="utf-8">
<title>Corvane Trading – Business Card</title>
<link href="https://fonts.googleapis.com/css2?family=Roboto:wght@400;500&family=Saira+Condensed:wght@500&display=swap" rel="stylesheet">
<style>
  :root {
    --bg: #2b2b2c;
    --card: #ececec;
    --red: #b0202a;
    --grey: #858a90;
    --ink: #1e1e1e;
  }
  * { margin: 0; padding: 0; box-sizing: border-box; }
  html, body { width: 1200px; height: 1138px; overflow: hidden; }
  body { background: var(--bg); position: relative; font-family: "Roboto", Arial, sans-serif; }

  .card {
    position: absolute;
    width: 622px;
    height: 376px;
    background: var(--card);
    border-radius: 16px;
    overflow: hidden;
  }
  .card--front { left: 274px; top: 186px; }
  .card--back  { left: 276px; top: 607px; }

  /* Front */
  .front-brand {
    position: absolute;
    left: 0; right: 0; top: 150px;
    display: flex; align-items: center; justify-content: center; gap: 18px;
  }
  .brand-dot {
    width: 46px; height: 46px; border-radius: 50%;
    background: var(--red);
  }
  .brand-name {
    font-family: "Roboto", Arial, sans-serif;
    font-weight: 500;
    color: var(--red);
    letter-spacing: 0.08em;
    text-transform: uppercase;
    white-space: nowrap;
  }
  .front-brand .brand-name { font-size: 44px; }
  .front-stripe {
    position: absolute; left: 0; right: 0; bottom: 0; height: 11px;
    display: flex;
  }
  .front-stripe .red  { flex: 1; background: var(--red); }
  .front-stripe .grey { flex: 1; background: var(--grey); }

  /* Back */
  .back-info {
    position: absolute; right: 27px; top: 38px;
    text-align: right;
    color: var(--ink);
  }
  .back-info .brand-name { font-size: 30px; line-height: 1; }
  .person-name {
    margin-top: 96px;
    font-family: "Saira Condensed", "Arial Narrow", sans-serif;
    font-weight: 500;
    font-size: 26px;
    line-height: 1;
    color: var(--red);
  }
  .person-role { font-size: 16px; margin-top: 7px; }
  .address { font-size: 16px; line-height: 23px; margin-top: 20px; }
  .contacts { list-style: none; margin-top: 8px; }
  .contacts li {
    font-size: 16px; line-height: 23.5px;
    display: flex; justify-content: flex-end; align-items: center; gap: 14px;
  }
  .contacts svg { width: 16px; height: 16px; fill: var(--red); }
</style>
</head>
<body>

<section class="card card--front" aria-label="Card front">
  <div class="front-brand">
    <span class="brand-dot" aria-hidden="true"></span>
    <span class="brand-name">Corvane Trading</span>
  </div>
  <div class="front-stripe"><span class="red"></span><span class="grey"></span></div>
</section>

<section class="card card--back" aria-label="Card back">
  <div class="back-info">
    <div class="brand-name">Corvane Trading</div>
    <div class="person-name">Daniel Reyes</div>
    <div class="person-role">Managing Director</div>
    <p class="address">512 Harbor Rd., Port City,<br>Bay Town, US 654321</p>
    <ul class="contacts">
      <li>000-222-3333
        <svg viewBox="0 0 16 16" aria-hidden="true"><path d="M1 5c0-2 3-3 7-3s7 1 7 3v1h-4V4.5H5V6H1zM4 7h8l2 5v2H2v-2zm4 1.5a2 2 0 1 0 0 4 2 2 0 0 0 0-4z"/></svg>
      </li>
      <li>daniel@corvanetrading.com
        <svg viewBox="0 0 16 16" aria-hidden="true"><path d="M1 3h14v10H1zm1.5 1.5v.3L8 9l5.5-4.2v-.3zm0 2.2v4.8h11V6.7L8 10.9z"/></svg>
      </li>
      <li>www.corvanetrading.com
        <svg viewBox="0 0 16 16" aria-hidden="true"><path d="M8 1a7 7 0 1 0 0 14A7 7 0 0 0 8 1zm-.7 1.6v2.6H5.2c.4-1.3 1.2-2.3 2.1-2.6zm1.4 0c.9.3 1.7 1.3 2.1 2.6H8.7zM3.8 5.2H2.9a5.6 5.6 0 0 1 2-2.2 6 6 0 0 0-1.1 2.2zm8.4 0a6 6 0 0 0-1.1-2.2 5.6 5.6 0 0 1 2 2.2zM2.5 6.6h1.1a10 10 0 0 0 0 2.8H2.5a5.6 5.6 0 0 1 0-2.8zm2.5 0h2.3v2.8H5a8 8 0 0 1 0-2.8zm3.7 0H11a8 8 0 0 1 0 2.8H8.7zm3.7 0h1.1a5.6 5.6 0 0 1 0 2.8h-1.1a10 10 0 0 0 0-2.8zM2.9 10.8h.9a6 6 0 0 0 1.1 2.2 5.6 5.6 0 0 1-2-2.2zm2.3 0h2.1v2.6c-.9-.3-1.7-1.3-2.1-2.6zm3.5 0h2.1c-.4 1.3-1.2 2.3-2.1 2.6zm3.5 0h.9a5.6 5.6 0 0 1-2 2.2 6 6 0 0 0 1.1-2.2z"/></svg>
      </li>
    </ul>
  </div>
</section>

</body>
</html>
```